Meridale Wall Tracking Office

I have a current web site that it looking quite aged and it needs a new lease of life. This is a Graffiti Management Website so is all about data processing and management of information. I want a html 5 view on any platform design. clean crisp and new. I have provided some screen shots of my current site.

Target Market(s)

The Target Market will be local government. most users will not be heavy pc users

Industry/Entity Type

Management

Font styles to use
Sans Serif
Other font styles liked:
• web font like calibri

Colors

Designer to choose colors to be used in the design.

Requirements
Must have
• Must have menus similar to attachments

```html
<!DOCTYPE html>
<html lang="en">
<head>
<meta charset="utf-8">
<title>Meridale Wall Tracking Office – Job Photos</title>
<link rel="stylesheet" href="https://fonts.googleapis.com/css2?family=Carlito:wght@400;700&family=Lato:wght@900&display=swap">
<style>
  :root {
    --teal: #10d3b7;
    --teal-light: #12e2c6;
    --teal-dark: #07806e;
    --panel: rgba(16, 190, 165, 0.85);
    --white: #ffffff;
    --ink: #10302b;
    --field-border: #0a4d44;
    --field-fill: rgba(16, 220, 195, 0.6);
  }
  html, body {
    margin: 0;
    padding: 0;
    width: 1200px;
    height: 1166px;
    overflow: hidden;
    background: var(--white);
  }
  .page {
    position: relative;
    width: 1200px;
    height: 1166px;
    overflow: hidden;
    font-family: "Carlito", "Lato", sans-serif;
  }
  .banner-art {
    position: absolute;
    left: 0;
    width: 1200px;
  }
  .banner-art--top {
    top: 0;
    height: 254px;
    background: linear-gradient(100deg, #c98e86 0%, #3b7fb8 22%, #c2575a 42%, #2f9ad0 60%, #b74c53 80%, #3a86c2 100%);
  }
  .banner-art--bottom {
    top: 879px;
    height: 287px;
    background: linear-gradient(95deg, #c6a650 0%, #3a3c56 18%, #46b84c 40%, #2f6a86 62%, #3fa33c 78%, #2d3e70 100%);
  }
  .masthead {
    position: absolute;
    left: 104px;
    top: 44px;
    width: 990px;
    height: 131px;
    background: var(--panel);
    border-radius: 4px;
    box-shadow: 4px 5px 6px rgba(0,0,0,0.55);
  }
  .masthead__name {
    position: absolute;
    left: 19px;
    top: 35px;
    margin: 0;
    font-family: "Lato", sans-serif;
    font-weight: 900;
    font-size: 48px;
    line-height: 60px;
    color: var(--white);
    white-space: nowrap;
  }
  .workspace {
    position: absolute;
    left: 0;
    top: 254px;
    width: 1200px;
    height: 625px;
    background: radial-gradient(ellipse 70% 90% at 55% 45%, var(--teal-light) 0%, var(--teal) 45%, var(--teal-dark) 100%);
  }
  .sidebar {
    position: absolute;
    left: 10px;
    top: 272px;
    width: 310px;
    height: 651px;
    background: linear-gradient(180deg, #4a4546 0%, #6a4a4e 35%, #58494c 70%, #3d3a3b 100%);
    box-shadow: 3px 3px 6px rgba(0,0,0,0.6);
  }
  .nav__item {
    position: absolute;
    left: 5px;
    width: 309px;
    height: 53px;
    background: linear-gradient(180deg, var(--teal-light), var(--teal));
    color: var(--white);
    font-family: "Carlito", sans-serif;
    font-weight: 700;
    font-size: 25px;
    line-height: 53px;
    text-align: center;
    text-transform: uppercase;
    letter-spacing: 1.5px;
    text-decoration: none;
    white-space: nowrap;
  }
  .nav__item--logout {
    font-size: 33px;
    font-weight: 400;
  }
  .field-label {
    position: absolute;
    left: 361px;
    font-size: 25px;
    line-height: 32px;
    color: var(--white);
    white-space: nowrap;
  }
  .field-input {
    position: absolute;
    left: 589px;
    width: 436px;
    height: 30px;
    border: 1px solid var(--field-border);
    background: var(--field-fill);
  }
  .btn {
    position: absolute;
    background: var(--white);
    border-radius: 4px;
    box-shadow: 3px 3px 4px rgba(0,0,0,0.45);
    color: var(--ink);
    text-align: center;
  }
  .btn--save {
    left: 1072px;
    width: 108px;
    height: 35px;
    font-size: 24px;
    line-height: 35px;
    letter-spacing: 1px;
  }
  .btn--ok {
    left: 623px;
    top: 540px;
    width: 152px;
    height: 56px;
    font-size: 40px;
    line-height: 56px;
  }
</style>
</head>
<body>
<div class="page">
  <div class="banner-art banner-art--top" role="img" aria-label="Colourful spray-painted graffiti mural on a brick wall"></div>
  <div class="banner-art banner-art--bottom" role="img" aria-label="Green and blue graffiti lettering mural with characters"></div>

  <header class="masthead">
    <h1 class="masthead__name">Meridale Wall Tracking Office</h1>
  </header>

  <main class="workspace">
    <form class="photo-form">
      <label class="field-label" style="top:204px">Add Graffiti Photo</label>
      <div class="field-input" style="top:203px"></div>
      <div class="btn btn--save" style="top:202px">SAVE</div>

      <label class="field-label" style="top:284px">Add Cleaned Photo</label>
      <div class="field-input" style="top:283px"></div>
      <div class="btn btn--save" style="top:283px">SAVE</div>

      <label class="field-label" style="top:362px; left:366px">Delet Photo Name</label>
      <div class="field-input" style="top:361px"></div>

      <div class="btn btn--ok">OK</div>
    </form>
  </main>

  <nav class="sidebar">
    <a class="nav__item" style="top:19px">Home User</a>
    <a class="nav__item" style="top:85px">Add&nbsp; a&nbsp; job</a>
    <a class="nav__item" style="top:154px">Current Jobs</a>
    <a class="nav__item" style="top:225px">Closed Jobs</a>
    <a class="nav__item" style="top:294px">Search Jobs</a>
    <a class="nav__item" style="top:362px">Reports</a>
    <a class="nav__item" style="top:428px">User Details</a>
    <a class="nav__item" style="top:497px">Admin</a>
    <a class="nav__item nav__item--logout" style="top:576px">LOG OUT</a>
  </nav>
</div>
</body>
</html>
```